Lumeno-Interior design firm
Hello all,
I will announce the winner in the next few hours...
I appreciate your AMAZING ideas and all the many revisions that each of you submited, they helped us to understand your creative proposals and at the end to select a winner.
THANK YOU!
Lumeno Design
Draft #317 and #318
We are looking at some winning designs already and we will send our efforts towards those. i appreciate your entry very much.
Thanks!
Draft #312
The font on the subject LUMENO Interior design firm needs to be changed. I dont like it. I like the font used on the HOME, PORTFOLIO, etc...main subjects if that helps!
Everything else looks amazing!
hi all,
I had an unexpected business to attend today and I was not able to complete the feedback to all of you. We decided to extend the time to provide the missing feedback...I will provide to all, just give me some time.
I have decided to extend the contest. This was a last minute descision.
I appreciate your entry but is not what I am looking for. I don't want to waste your time as well as I prefer to concentrate on the designs/designers that have invested some time with me already.
Thank you and I appreciate your understanding!
Thanks brightquill! I really appreciate your understanding!
Draft #273
Can you justified all the texts used on each page? That will be great for final review.
Drafts #270 and #272
the text needs to be justified and that will make it!
Draft #269
HOME
There is a small misspell at the bottom left...it reads Lemeno instead of Lumeno.
Ater that revision you are set!
@PH, Thanks for your comments...
Dear Brightquill,
I like your entry but i am sorry to say that there is nothing original about it. I feel respect for everyones work and even when I am not an expert I feel you are copying other entries. I can not give you credit for someone else's ideas and I would appreciate if you come up with the same concept but with something that is your very own creation.
With all my respect...
Draft #251
Looks good just to revise the "yellow" cubes to be softer...and also please use my pictures for each page so I can compare with everyone else.
Thank you so much!
Draft #250
I would prefer to container the ABOUT US description on within the limits of the cubes so if necessary lets remove the "yellow" cubes so we can move up the wording and fit it within...
Use the service wording as reference...it is contained and it does not go below the "cubes"
Draft #249
lets list the services on a horizontal way inside the "cubes" Makes sense? linear way showing the services and the main wording as is.
Draft #248
can we made the windows with tabs LIVING, DINING, BEDROOM ACCENTS and KIDS to be one of the "cubes" from your design?
maybe using the bottom five...?
then when you click on I would like to see a complete picture...hopefully you come up with an idea but if not we can look at it together after revision...
Thanks
Draft #247
My only change is the "yellow" buttons to be more with softer colors...soft grey/white...or any suggestions within my request.
Draft #234
Wording needs to be consistent...I prefer white please revise.
Draft #227
Revisions:
I dont like the phone image under phone, please remove
Please do not underline the website
I prefer just letter on the front:
P: for phone
W: for website
etc...
In your case I would prefer not to use my picture...lets just remove it and after all this it should be done!
Looking good!
Draft #223
I need you to add the wording that I sent for services as well...it is important!
Thanks! Everything else looks perfect!
Hello@PH
I`m just waiting for your Feedback on
#221(Home page), #222(Portfolio Page), #223(Services Page),#224(About Us Page), & #225(Contact Page)
Zora
FOR EVERYONE:
PLEASE submit your complete designs, I wont be extending the project and with the time left I wont be able to give feedback and revisions to detail to everyone.
I really appreciate your hard work on attention to my project.
You ALL are very talented!
Good luck!
Draft #208 you can move forward with the inner pages.
Draft #207
I need the text to be justified please. You can complete your design with all he pages, I like the layout as is.
Look forward to final entries.

```html
<!DOCTYPE html>
<html lang="en">
<head>
<meta charset="utf-8">
<title>Lumeno | Interior Design, Architecture, Art</title>
<link href="https://fonts.googleapis.com/css2?family=Josefin+Sans:wght@300&family=Arimo:wght@400;700&display=swap" rel="stylesheet">
<style>
  :root {
    --page-bg: #e7e6e1;
    --brand-ink: #8b8a84;
    --tagline-ink: #77766f;
    --frame: #f7f7f5;
    --photo-light: #d9d3c8;
    --photo-mid: #a99f90;
    --photo-dark: #5e5246;
    --panel: rgba(255, 255, 255, 0.22);
    --panel-edge: rgba(255, 255, 255, 0.35);
    --text-light: #ffffff;
    --nav-muted: #d8d4cc;
    --footer-ink: #9a9992;
    --social: #8e9cae;
  }
  * { box-sizing: border-box; margin: 0; padding: 0; }
  html, body {
    width: 1200px; height: 901px; overflow: hidden;
    background: var(--page-bg);
    font-family: "Arimo", Arial, sans-serif;
  }
  .page { position: relative; width: 1200px; height: 901px; }

  .brand { position: absolute; left: 272px; top: 40px; }
  .brand-name {
    font-family: "Josefin Sans", sans-serif; font-weight: 300;
    font-size: 72px; line-height: 1; letter-spacing: 4px;
    color: var(--brand-ink);
  }
  .brand-tagline {
    margin-top: 4px;
    font-family: "Josefin Sans", sans-serif; font-weight: 300;
    font-size: 21px; color: var(--tagline-ink); letter-spacing: 0.5px;
  }

  .stage {
    position: absolute; left: 117px; top: 161px;
    width: 971px; height: 591px;
    border: 3px solid var(--frame);
    overflow: hidden;
  }
  .stage-photo {
    position: absolute; inset: 0;
    background:
      linear-gradient(180deg, rgba(255,255,255,0.15) 0%, rgba(0,0,0,0) 40%, rgba(40,30,20,0.35) 100%),
      linear-gradient(90deg, var(--photo-light) 0%, var(--photo-mid) 45%, var(--photo-light) 65%, var(--photo-dark) 100%);
  }

  .about-title {
    position: absolute; left: 85px; top: 358px;
    font-size: 19px; font-weight: 700; color: var(--text-light); letter-spacing: 0.5px;
  }
  .about-col {
    position: absolute; top: 400px; width: 222px; height: 176px;
    padding: 9px 10px;
    background: var(--panel);
    border: 1px solid var(--panel-edge);
    color: var(--text-light);
    font-size: 12.5px; line-height: 17px;
    text-align: justify;
  }
  .col-1 { left: 73px; }
  .col-2 { left: 314px; }
  .col-3 { left: 557px; }

  .main-nav {
    position: absolute; right: 20px; top: 412px;
    list-style: none; text-align: right;
  }
  .main-nav li {
    font-size: 17px; line-height: 29px; color: var(--text-light);
    letter-spacing: 0.3px;
  }
  .main-nav li.current { color: var(--nav-muted); }

  .footer-note {
    position: absolute; left: 117px; top: 873px;
    font-size: 12.5px; color: var(--footer-ink);
  }
  .follow {
    position: absolute; left: 940px; top: 869px;
    display: flex; align-items: center; gap: 10px;
    font-size: 12.5px; color: var(--footer-ink);
  }
  .social { display: flex; align-items: center; gap: 4px; color: var(--social); }
  .social-dot { width: 10px; height: 10px; background: var(--social); }
</style>
</head>
<body>
<div class="page">
  <header class="brand">
    <div class="brand-name">LUMENO</div>
    <div class="brand-tagline">Interior Design • Architecture • Art</div>
  </header>

  <section class="stage">
    <div class="stage-photo" role="img" aria-label="Photograph of an elegant dining room with white slip-covered chairs, a long table, a pendant lamp and a curved staircase"></div>

    <h2 class="about-title">ABOUT US</h2>
    <p class="about-col col-1">We are an interior design firm with several years practice founded &amp; established in Maple Hollow, Oregon. Our goal is to provide a superb experience to our clients under the guidance of our founder Architect Elena Varga and her extraordinary eye on design.</p>
    <p class="about-col col-2">She is National Sales and Operations Manager for a nationwide high end furniture company and has held on her expertise over 500 home designs. We pride on achieving the highest standards for the industry by creating not just experiences but every day.</p>
    <p class="about-col col-3">enjoyable memories through our design process. We have the skills, experience and staff to completely detail and furnish your home creating the most dramatic and sophisticated ambience according to your needs and style.</p>

    <ul class="main-nav">
      <li>HOME</li>
      <li>PORTFOLIO</li>
      <li>SERVICES</li>
      <li class="current">ABOUT US</li>
      <li>CONTACT</li>
    </ul>
  </section>

  <footer>
    <p class="footer-note">Copyright 2011, All Rights Reserved. LUMENO | Interior Design, Architecture, Art</p>
    <div class="follow">
      <span>Follow Us On</span>
      <span class="social"><span class="social-dot"></span>Kindra</span>
      <span class="social">Chirpo</span>
    </div>
  </footer>
</div>
</body>
</html>
```